Cardiology Practice needs a Heart Scan Order Form

Busy cardiology practice needs an order form for a heart scan test. Sample is attached. One side should have all information noted and the other side should have our physician names (Vikram Joshi, MD, K.L. Morvandi, MD, Anjali Desai, MD, Parvin Joshi, MD, and Gerald Montefino, MD. It should have the map that is uploaded and our demographic information (Crestline Cardio PLLC, 218 Juniper Ave. Ste. B, Webster, TX 77412 along with phone 713-642-1187 and fax 713-642-1188) as well as our web address (crestlinecardio.example). Our primary colors are red, black and white. Needs to fit paper size 8 1/2 by 11.

Target Market(s)

Healthcare

Industry/Entity Type

Health Care

Font styles to use
Serif

Colors
ec1f27

Requirements
Must have
• Logo, information listed on sample form, demographics and physician names as well as website.
Nice to have
• Open to suggestions
Should not have
• Physician Pictures

```html
<!DOCTYPE html>
<html lang="en">
<head>
<meta charset="utf-8">
<title>Crestline Cardio – Calcium Score Heart Scan Order Form</title>
<link rel="stylesheet" href="https://fonts.googleapis.com/css2?family=Montserrat:ital,wght@0,400;0,500;0,600;0,700;0,800;1,500;1,600&family=Roboto+Condensed:ital,wght@0,400;0,700;1,700&display=swap">
<style>
:root{
  --red:#bf2e37;
  --ink:#1c1c1c;
  --muted:#3a3a3a;
  --paper:#ffffff;
  --backdrop:#7a7a7a;
  --map-base:#e9e7e3;
  --map-warm:#f3e2b8;
}
*{box-sizing:border-box;margin:0;padding:0}
html,body{width:1200px;height:893px;overflow:hidden}
body{background:var(--backdrop);font-family:"Montserrat",sans-serif;color:var(--ink);position:relative}
.page{position:absolute;top:81px;width:505px;height:715px;background:var(--paper)}
.page--form{left:74px}
.page--cover{left:626px}
.abs{position:absolute}

/* brand */
.brand{display:flex;align-items:center;gap:6px;font-weight:800;color:var(--red);letter-spacing:.04em;white-space:nowrap}
.brand__dot{width:12px;height:12px;border-radius:50%;background:var(--red);flex:none}
.brand--small{left:29px;top:40px;font-size:17px}
.brand--large{left:0;right:0;top:82px;justify-content:center;font-size:32px;gap:10px}
.brand--large .brand__dot{width:24px;height:24px}

/* form header */
.form-title{right:27px;top:26px;text-align:right;font-weight:700;font-size:17.5px;line-height:19px}
.form-title span{display:block;color:var(--red);font-weight:600}
.head-rule{left:108px;right:0;top:67px;height:2px;background:var(--red)}

.section-label{left:27px;top:114px;color:var(--red);font-weight:600;font-size:11.5px}
.band{left:27px;width:451px;height:18px;background:var(--red);color:#fff;font-weight:600;font-size:10px;display:flex;align-items:center;justify-content:center}

.row{left:27px;width:451px;display:flex;gap:3px;font-size:10px;align-items:flex-end;white-space:nowrap}
.fill{flex:1;border-bottom:1px dotted var(--ink);height:8px;margin-bottom:2px}
.fill--s{flex:0 0 var(--w)}
.row b{font-weight:600}

.checks{left:27px;width:451px;display:flex;justify-content:space-between;font-size:10px;white-space:nowrap}
.box{display:inline-block;width:8px;height:8px;border:1px solid var(--red);margin-right:3px;vertical-align:-1px}
.dots{display:inline-block;border-bottom:1px dotted var(--ink);width:var(--w);height:1px}

.notice{left:27px;width:451px;font-family:"Roboto Condensed",sans-serif;font-style:italic;font-weight:700;font-size:7.2px}
.rules{left:27px;width:420px;list-style:none;font-family:"Roboto Condensed",sans-serif;font-size:7px;line-height:8.4px;color:var(--muted)}
.rules li{display:flex;gap:5px}
.rules .box{width:6.5px;height:6.5px;flex:none;margin:1px 0 0}
.ack{left:27px;width:451px;font-family:"Roboto Condensed",sans-serif;font-size:7px;line-height:10px;color:var(--muted)}

.sign{width:145px;border-top:1.5px solid var(--red);padding-top:3px;font-style:italic;font-weight:600;font-size:9.5px}
.ref{left:339px;top:581px;width:139px;border:1px solid var(--red);font-family:"Roboto Condensed",sans-serif;font-size:7px}
.ref__head{background:var(--red);color:#fff;padding:2px 5px;height:13px}
.ref__cell{border-top:1px solid var(--red);padding:4px 5px;height:18px}

.form-foot{left:0;right:0;top:672px;text-align:center;font-size:9.4px;line-height:12.5px}

/* cover */
.physicians{left:0;right:0;top:169px;text-align:center;color:var(--red);font-weight:700;font-size:19.5px;line-height:23.5px;letter-spacing:.01em}
.map{left:32px;top:262px;width:445px;height:317px;border:2px solid var(--red);border-radius:12px;
  background:linear-gradient(135deg,var(--map-warm) 0%,var(--map-base) 35%,var(--map-base) 70%,#dcdad6 100%)}
.address{left:0;right:0;top:597px;text-align:center;font-size:14.5px;line-height:18.5px;color:var(--muted)}
.web{left:0;right:0;top:666px;text-align:center;color:var(--red);font-weight:700;font-size:15.5px}
</style>
</head>
<body>

<section class="page page--form">
  <div class="abs brand brand--small"><span class="brand__dot"></span>CRESTLINE CARDIO</div>
  <h1 class="abs form-title">CALCIUM SCORE<span>HEART SCAN</span></h1>
  <div class="abs head-rule"></div>

  <h2 class="abs section-label">TEST SCHEDULE</h2>
  <div class="row abs" style="top:129px"><b>Test date:</b><span class="fill fill--s" style="--w:90px"></span><span style="flex:1"></span><b>Test time:</b><span class="fill fill--s" style="--w:137px"></span></div>

  <div class="abs band" style="top:157px">PATIENT INFORMATION</div>
  <div class="row abs" style="top:182px">Name:<span class="fill"></span>MI:<span class="fill fill--s" style="--w:180px"></span></div>
  <div class="row abs" style="top:203px">Date of birth:<span class="fill"></span>Account no:<span class="fill fill--s" style="--w:175px"></span></div>

  <div class="abs band" style="top:225px">CONTACT INFORMATION</div>
  <div class="row abs" style="top:252px">Address:<span class="fill"></span></div>
  <div class="row abs" style="top:273px">Home phone no:<span class="fill"></span>Mobile phone no:<span class="fill fill--s" style="--w:140px"></span></div>

  <div class="abs band" style="top:296px">MEDICAL INFORMATION</div>
  <div class="row abs" style="top:324px">Sex:<span class="fill fill--s" style="--w:48px"></span>Height:<span class="fill fill--s" style="--w:68px"></span>Weight:<span class="fill fill--s" style="--w:60px"></span>Race:<span class="fill"></span></div>
  <div class="row abs" style="top:344px">Diagnosis:<span class="fill"></span></div>
  <div class="checks abs" style="top:365px">
    <span><i class="box"></i>PCI (no. of stents:<i class="dots" style="--w:32px"></i>)</span>
    <span><i class="box"></i>CABG (no. of vessels:<i class="dots" style="--w:32px"></i>)</span>
    <span><i class="box"></i>MI (last event:<i class="dots" style="--w:44px"></i>)</span>
    <span><i class="box"></i>PCM/ICD</span>
  </div>
  <div class="checks abs" style="top:386px">
    <span><i class="box"></i>Diabetes</span><span><i class="box"></i>Claustrophobia</span><span><i class="box"></i>Asthma</span><span><i class="box"></i>Emphysema</span><span><i class="box"></i>COPD</span>
  </div>
  <div class="checks abs" style="top:406px">
    <span>LMP: <i class="dots" style="--w:72px"></i></span><span><i class="box"></i>bHCG</span><span><i class="box"></i>Tubal ligation</span><span><i class="box"></i>Post-menopause &gt; 1 year</span><span><i class="box"></i>Hysterectomy</span>
  </div>

  <p class="abs notice" style="top:429px">Please read the following instructions carefully. You might be rescheduled if any of the following instructions are not met.</p>
  <ul class="abs rules" style="top:444px">
    <li><i class="box"></i><span>AVOID <b>caffeine</b> containing products (coffee, tea, soda, chocolate, energy drinks, or some over the counter medications) for 4 hours prior to testing.</span></li>
    <li><i class="box"></i><span>AVOID <b>smoking</b> for 4 hours prior to testing.</span></li>
    <li><i class="box"></i><span>AVOID <b>eating</b> or <b>drinking</b> anything except water for 4 hours prior to testing.</span></li>
    <li><i class="box"></i><span>Arrive <u>15 minutes</u> early for your appointment time.</span></li>
    <li><i class="box"></i><span>Wear comfortable clothing. <u>Remove any metal objects</u>, such as jewelry or piercings. Women will be asked to remove bras containing metal underwire.</span></li>
    <li><i class="box"></i><span>Inform your physician or the staff if you are claustrophobic or have a problem staying in restricted environments for any length of time.</span></li>
    <li><i class="box"></i><span>Inform the physician or the staff if you are or think you might be pregnant.</span></li>
  </ul>
  <p class="abs ack" style="top:550px">I hereby acknowledge that the instructions and procedures pertinent to this study were explained thoroughly, I had time to ask questions, and these questions were addressed satisfactorily.</p>

  <div class="abs sign" style="left:27px;top:595px">Patient's print name</div>
  <div class="abs sign" style="left:178px;top:595px">Patient's signature</div>
  <div class="abs sign" style="left:27px;top:636px">Prescriber's print name</div>
  <div class="abs sign" style="left:178px;top:636px">Prescriber's signature</div>

  <div class="abs ref">
    <div class="ref__head">Referring physician contact information</div>
    <div class="ref__cell">Order date:</div>
    <div class="ref__cell">Tel no:</div>
    <div class="ref__cell">Fax no:</div>
  </div>

  <p class="abs form-foot">Crestline Cardio, PLLC. Visit us at 218 Juniper Ave., Ste. B, Webster, TX 77412.<br>For appointments or more information on testing, please call (713) 642 1187, or visit crestlinecardio.example.</p>
</section>

<section class="page page--cover">
  <div class="abs brand brand--large"><span class="brand__dot"></span>CRESTLINE CARDIO</div>
  <p class="abs physicians">VIKRAM JOSHI, M.D. | K.L. MORVANDI, M.D.<br>ANJALI DESAI, M.D. | PARVIN JOSHI, M.D.<br>GERALD MONTEFINO, M.D.</p>
  <div class="abs map" role="img" aria-label="Street map showing the clinic location on Juniper Ave. in Webster, TX"></div>
  <p class="abs address">CRESTLINE CARDIO PLLC<br>218 JUNIPER AVE. STE. B, WEBSTER, TX 77412<br>PHONE 713-642-1187 &amp; FAX 713-642-1188</p>
  <p class="abs web">CRESTLINECARDIO.EXAMPLE</p>
</section>

</body>
</html>
```